Fun A1 2012 family planner using clever typography and block colour

I have been looking for an A1 2012 family planner and I have not been able to find one. Hence I would like help to develop such a planner. I plan to print it on matt paper, portrait orientated. I have attached some reference pictures of our 2011 planner. I like interesting typography, clear clean colours and simple illustration. I need space to write in daily events and need the weeks and days to be clearly delineated from each other. Each day cell needs the date and day in it (please refer to the file uploaded for a visual reference confirming this). Each weekend needs some kind of colour/ typographic delineation. I want a design for a year-at-a-view calendar. I plan to print the planner in Sydney, Australia with plinthworkprints.com.au and probably to sell printed copies online. The terms & conditions of this project are that I will own the design concept 100% and in perpetuity worldwide once payment has been made. (NB. The attached Work File in Word contains a rough layout and all months, days and dates all typed up to make for quicker design.)

Target Market(s)

Reasonably well heeled family of 4. 2 parents. 2 kids. 2 pets.

Industry/Entity Type

Events

Requirements
Must have
• The calendar must be portrait (not landscape orientated), A1 size. It will be printed on matt paper by plinthworkprints.com.au. It must have months running left to right (Jan-Dec) and day/date cells running top to bottom (refer 2011 planner photos in file uploaded). The day/ date cells must be around 3(w)x2(h)cm - big enough to write daily events in. Weekends must be colour/ typographically delineated. 2012 year must be noted as must "A Lanternmoss Inc Project" and web address in fine print bottom left hand left hand corner.
Nice to have
• A Lanternmoss Inc logo in bottom left hand corder (perhaps Nimble Heron like: http://www.artquarry.com/design_submission.aspx?designid=614307). Header/Footer space for customisation (e.g. "Dunmore-Pratt 2012 Planner" or "XYZ Co 2012 Planner".
Should not have
• The calendar should not use photographs or resemble standard or cheesy wall calendars. No watermarks please.

```html
<!DOCTYPE html>
<html lang="en">
<head>
<meta charset="utf-8">
<title>XYZ Co 2012 Planner</title>
<link rel="stylesheet" href="https://fonts.googleapis.com/css2?family=Nunito:wght@600;800;900&display=swap">
<style>
:root{
  --green-band:#8dc63f;--green-head:#4d7a27;--green-cell:#f4f8ef;--green-mark:#d4e8c8;
  --leaf-band:#39b54a;--leaf-head:#0f6a34;--leaf-cell:#f1f7f1;--leaf-mark:#c7e3c5;
  --amber-band:#fbb040;--amber-head:#8c6324;--amber-cell:#fff8ee;--amber-mark:#fde2bd;
  --orange-band:#f37021;--orange-head:#8d3f0f;--orange-cell:#fef4ee;--orange-mark:#fbd1b4;
  --red-band:#ed1c24;--red-head:#8b0f14;--red-cell:#fdf2ef;--red-mark:#f6c1b3;
  --wine-band:#9e1c20;--wine-head:#680a0d;--wine-cell:#f9efed;--wine-mark:#ddb3a8;
  --ink:#1e1e1e;--holiday:#f26522;--white:#fff;
}
*{box-sizing:border-box;margin:0;padding:0}
html,body{width:847px;height:1200px;overflow:hidden}
body{font-family:"Nunito",sans-serif;color:var(--ink)}
.planner{position:relative;width:847px;height:1200px;display:flex;
  background:linear-gradient(90deg,var(--green-band) 0 29.6px,transparent 29.6px calc(100% - 29.6px),var(--wine-band) calc(100% - 29.6px))}
.month{width:65.65px;margin-left:0;padding:30px 0 30px;background:var(--band);display:flex;flex-direction:column}
.month:first-child{margin-left:29.6px}
.g1{--band:var(--green-band);--head:var(--green-head);--cell:var(--green-cell);--mark:var(--green-mark)}
.g2{--band:var(--leaf-band);--head:var(--leaf-head);--cell:var(--leaf-cell);--mark:var(--leaf-mark)}
.o1{--band:var(--amber-band);--head:var(--amber-head);--cell:var(--amber-cell);--mark:var(--amber-mark)}
.o2{--band:var(--orange-band);--head:var(--orange-head);--cell:var(--orange-cell);--mark:var(--orange-mark)}
.r1{--band:var(--red-band);--head:var(--red-head);--cell:var(--red-cell);--mark:var(--red-mark)}
.r2{--band:var(--wine-band);--head:var(--wine-head);--cell:var(--wine-cell);--mark:var(--wine-mark)}
.month h2{height:49px;background:var(--head);color:var(--white);font-weight:900;font-size:21px;
  text-align:center;line-height:52px;letter-spacing:.3px}
.days{list-style:none;background:var(--white);height:1038.5px;display:flex;flex-direction:column;padding:0 1px}
.day{position:relative;height:33.5px;background:var(--cell);border-radius:4px;margin-top:0;
  padding:3px 0 0 5px;border-top:1.5px solid var(--white)}
.day::before{content:"";position:absolute;left:-3px;top:-3px;width:5px;height:5px;background:var(--band);transform:rotate(45deg)}
.day.mark{background:var(--mark)}
.day b{display:block;font-weight:800;font-size:13.5px;line-height:14px}
.day small{display:block;font-weight:600;font-size:7px;line-height:8px}
.day.hol b{color:var(--holiday)}
.foot{height:52px;background:var(--head)}
.title{position:absolute;left:40px;top:1127px;color:var(--white);font-weight:800;font-size:26px;letter-spacing:.3px}
</style>
</head>
<body>
<main class="planner">

<section class="month g1"><h2>JAN</h2><ol class="days">
<li class="day hol"><b>01</b><small>Sun</small></li><li class="day"><b>02</b><small>Mon</small></li><li class="day"><b>03</b><small>Tue</small></li><li class="day"><b>04</b><small>Wed</small></li><li class="day"><b>05</b><small>Thu</small></li><li class="day"><b>06</b><small>Fri</small></li><li class="day hol"><b>07</b><small>Sat</small></li><li class="day hol"><b>08</b><small>Sun</small></li><li class="day"><b>09</b><small>Mon</small></li><li class="day"><b>10</b><small>Tue</small></li><li class="day"><b>11</b><small>Wed</small></li><li class="day"><b>12</b><small>Thu</small></li><li class="day"><b>13</b><small>Fri</small></li><li class="day hol"><b>14</b><small>Sat</small></li><li class="day hol"><b>15</b><small>Sun</small></li><li class="day"><b>16</b><small>Mon</small></li><li class="day"><b>17</b><small>Tue</small></li><li class="day"><b>18</b><small>Wed</small></li><li class="day"><b>19</b><small>Thu</small></li><li class="day"><b>20</b><small>Fri</small></li><li class="day hol"><b>21</b><small>Sat</small></li><li class="day hol"><b>22</b><small>Sun</small></li><li class="day"><b>23</b><small>Mon</small></li><li class="day"><b>24</b><small>Tue</small></li><li class="day"><b>25</b><small>Wed</small></li><li class="day"><b>26</b><small>Thu</small></li><li class="day"><b>27</b><small>Fri</small></li><li class="day hol"><b>28</b><small>Sat</small></li><li class="day hol"><b>29</b><small>Sun</small></li><li class="day"><b>30</b><small>Mon</small></li><li class="day"><b>31</b><small>Tue</small></li>
</ol><div class="foot"></div></section>

<section class="month g2"><h2>FEB</h2><ol class="days">
<li class="day"><b>01</b><small>Wed</small></li><li class="day"><b>02</b><small>Thu</small></li><li class="day"><b>01</b><small>Wed</small></li><li class="day mark"><b>02</b><small>Thu</small></li><li class="day mark"><b>01</b><small>Wed</small></li><li class="day mark"><b>02</b><small>Thu</small></li><li class="day mark"><b>01</b><small>Wed</small></li><li class="day mark"><b>01</b><small>Wed</small></li><li class="day"><b>02</b><small>Thu</small></li><li class="day"><b>01</b><small>Wed</small></li><li class="day mark"><b>02</b><small>Thu</small></li><li class="day mark"><b>01</b><small>Wed</small></li><li class="day mark"><b>02</b><small>Thu</small></li><li class="day"><b>01</b><small>Wed</small></li><li class="day"><b>01</b><small>Wed</small></li><li class="day mark"><b>02</b><small>Thu</small></li><li class="day mark"><b>01</b><small>Wed</small></li><li class="day mark"><b>02</b><small>Thu</small></li><li class="day mark"><b>01</b><small>Wed</small></li><li class="day"><b>02</b><small>Thu</small></li><li class="day"><b>01</b><small>Wed</small></li><li class="day"><b>01</b><small>Wed</small></li><li class="day"><b>02</b><small>Thu</small></li><li class="day mark"><b>01</b><small>Wed</small></li><li class="day mark"><b>02</b><small>Thu</small></li><li class="day mark"><b>01</b><small>Wed</small></li><li class="day mark"><b>02</b><small>Thu</small></li><li class="day mark"><b>01</b><small>Wed</small></li><li class="day"><b>01</b><small>Wed</small></li><li class="day"><b>02</b><small>Thu</small></li><li class="day"><b>01</b><small>Wed</small></li>
</ol><div class="foot"></div></section>

<section class="month o1"><h2>MAR</h2><ol class="days">
<li class="day"><b>01</b><small>Thu</small></li><li class="day"><b>02</b><small>Fri</small></li><li class="day mark"><b>01</b><small>Thu</small></li><li class="day mark"><b>02</b><small>Fri</small></li><li class="day"><b>01</b><small>Thu</small></li><li class="day"><b>02</b><small>Fri</small></li><li class="day mark"><b>01</b><small>Thu</small></li><li class="day mark"><b>01</b><small>Thu</small></li><li class="day mark"><b>02</b><small>Fri</small></li><li class="day"><b>01</b><small>Thu</small></li><li class="day mark"><b>02</b><small>Fri</small></li><li class="day mark"><b>01</b><small>Thu</small></li><li class="day"><b>02</b><small>Fri</small></li><li class="day"><b>01</b><small>Thu</small></li><li class="day mark"><b>01</b><small>Thu</small></li><li class="day mark"><b>02</b><small>Fri</small></li><li class="day"><b>01</b><small>Thu</small></li><li class="day"><b>02</b><small>Fri</small></li><li class="day mark"><b>01</b><small>Thu</small></li><li class="day mark"><b>02</b><small>Fri</small></li><li class="day"><b>01</b><small>Thu</small></li><li class="day"><b>01</b><small>Thu</small></li><li class="day mark"><b>02</b><small>Fri</small></li><li class="day mark"><b>01</b><small>Thu</small></li><li class="day"><b>02</b><small>Fri</small></li><li class="day"><b>01</b><small>Thu</small></li><li class="day"><b>02</b><small>Fri</small></li><li class="day mark"><b>01</b><small>Thu</small></li><li class="day mark"><b>01</b><small>Thu</small></li><li class="day"><b>02</b><small>Fri</small></li><li class="day"><b>01</b><small>Thu</small></li>
</ol><div class="foot"></div></section>

<section class="month o2"><h2>APR</h2><ol class="days">
<li class="day hol"><b>01</b><small>Sun</small></li><li class="day"><b>02</b><small>Mon</small></li><li class="day mark"><b>01</b><small>Sun</small></li><li class="day mark"><b>02</b><small>Mon</small></li><li class="day"><b>01</b><small>Sun</small></li><li class="day"><b>02</b><small>Mon</small></li><li class="day"><b>01</b><small>Sun</small></li><li class="day"><b>01</b><small>Sun</small></li><li class="day"><b>02</b><small>Mon</small></li><li class="day"><b>01</b><small>Sun</small></li><li class="day mark"><b>02</b><small>Mon</small></li><li class="day mark"><b>01</b><small>Sun</small></li><li class="day"><b>02</b><small>Mon</small></li><li class="day mark"><b>01</b><small>Sun</small></li><li class="day mark"><b>01</b><small>Sun</small></li><li class="day"><b>02</b><small>Mon</small></li><li class="day"><b>01</b><small>Sun</small></li><li class="day"><b>02</b><small>Mon</small></li><li class="day"><b>01</b><small>Sun</small></li><li class="day mark"><b>02</b><small>Mon</small></li><li class="day mark"><b>01</b><small>Sun</small></li><li class="day"><b>01</b><small>Sun</small></li><li class="day mark"><b>02</b><small>Mon</small></li><li class="day mark"><b>01</b><small>Sun</small></li><li class="day"><b>02</b><small>Mon</small></li><li class="day"><b>01</b><small>Sun</small></li><li class="day"><b>02</b><small>Mon</small></li><li class="day"><b>01</b><small>Sun</small></li><li class="day"><b>01</b><small>Sun</small></li><li class="day"><b>02</b><small>Mon</small></li><li class="day"><b>01</b><small>Sun</small></li>
</ol><div class="foot"></div></section>

<section class="month r1"><h2>MAY</h2><ol class="days">
<li class="day"><b>01</b><small>Tue</small></li><li class="day"><b>02</b><small>Wed</small></li><li class="day mark"><b>01</b><small>Tue</small></li><li class="day mark"><b>02</b><small>Wed</small></li><li class="day"><b>01</b><small>Tue</small></li><li class="day"><b>02</b><small>Wed</small></li><li class="day"><b>01</b><small>Tue</small></li><li class="day"><b>01</b><small>Tue</small></li><li class="day"><b>02</b><small>Wed</small></li><li class="day"><b>01</b><small>Tue</small></li><li class="day mark"><b>02</b><small>Wed</small></li><li class="day mark"><b>01</b><small>Tue</small></li><li class="day"><b>02</b><small>Wed</small></li><li class="day mark"><b>01</b><small>Tue</small></li><li class="day mark"><b>01</b><small>Tue</small></li><li class="day"><b>02</b><small>Wed</small></li><li class="day"><b>01</b><small>Tue</small></li><li class="day"><b>02</b><small>Wed</small></li><li class="day"><b>01</b><small>Tue</small></li><li class="day mark"><b>02</b><small>Wed</small></li><li class="day mark"><b>01</b><small>Tue</small></li><li class="day"><b>01</b><small>Tue</small></li><li class="day mark"><b>02</b><small>Wed</small></li><li class="day mark"><b>01</b><small>Tue</small></li><li class="day"><b>02</b><small>Wed</small></li><li class="day"><b>01</b><small>Tue</small></li><li class="day"><b>02</b><small>Wed</small></li><li class="day"><b>01</b><small>Tue</small></li><li class="day"><b>01</b><small>Tue</small></li><li class="day"><b>02</b><small>Wed</small></li><li class="day"><b>01</b><small>Tue</small></li>
</ol><div class="foot"></div></section>

<section class="month r2"><h2>JUN</h2><ol class="days">
<li class="day"><b>01</b><small>Fri</small></li><li class="day hol"><b>02</b><small>Sat</small></li><li class="day mark"><b>01</b><small>Fri</small></li><li class="day mark"><b>02</b><small>Sat</small></li><li class="day"><b>01</b><small>Fri</small></li><li class="day"><b>02</b><small>Sat</small></li><li class="day"><b>01</b><small>Fri</small></li><li class="day"><b>01</b><small>Fri</small></li><li class="day"><b>02</b><small>Sat</small></li><li class="day"><b>01</b><small>Fri</small></li><li class="day mark"><b>02</b><small>Sat</small></li><li class="day mark"><b>01</b><small>Fri</small></li><li class="day"><b>02</b><small>Sat</small></li><li class="day mark"><b>01</b><small>Fri</small></li><li class="day mark"><b>01</b><small>Fri</small></li><li class="day"><b>02</b><small>Sat</small></li><li class="day"><b>01</b><small>Fri</small></li><li class="day"><b>02</b><small>Sat</small></li><li class="day"><b>01</b><small>Fri</small></li><li class="day mark"><b>02</b><small>Sat</small></li><li class="day mark"><b>01</b><small>Fri</small></li><li class="day"><b>01</b><small>Fri</small></li><li class="day mark"><b>02</b><small>Sat</small></li><li class="day mark"><b>01</b><small>Fri</small></li><li class="day"><b>02</b><small>Sat</small></li><li class="day"><b>01</b><small>Fri</small></li><li class="day"><b>02</b><small>Sat</small></li><li class="day"><b>01</b><small>Fri</small></li><li class="day"><b>01</b><small>Fri</small></li><li class="day"><b>02</b><small>Sat</small></li><li class="day"><b>01</b><small>Fri</small></li>
</ol><div class="foot"></div></section>

<section class="month g1"><h2>JUL</h2><ol class="days">
<li class="day hol"><b>01</b><small>Sun</small></li><li class="day"><b>02</b><small>Mon</small></li><li class="day"><b>01</b><small>Sun</small></li><li class="day mark"><b>02</b><small>Mon</small></li><li class="day mark"><b>01</b><small>Sun</small></li><li class="day"><b>02</b><small>Mon</small></li><li class="day"><b>01</b><small>Sun</small></li><li class="day"><b>01</b><small>Sun</small></li><li class="day"><b>02</b><small>Mon</small></li><li class="day"><b>01</b><small>Sun</small></li><li class="day mark"><b>02</b><small>Mon</small></li><li class="day mark"><b>01</b><small>Sun</small></li><li class="day"><b>02</b><small>Mon</small></li><li class="day mark"><b>01</b><small>Sun</small></li><li class="day mark"><b>01</b><small>Sun</small></li><li class="day"><b>02</b><small>Mon</small></li><li class="day"><b>01</b><small>Sun</small></li><li class="day"><b>02</b><small>Mon</small></li><li class="day"><b>01</b><small>Sun</small></li><li class="day mark"><b>02</b><small>Mon</small></li><li class="day mark"><b>01</b><small>Sun</small></li><li class="day"><b>01</b><small>Sun</small></li><li class="day"><b>02</b><small>Mon</small></li><li class="day mark"><b>01</b><small>Sun</small></li><li class="day mark"><b>02</b><small>Mon</small></li><li class="day"><b>01</b><small>Sun</small></li><li class="day"><b>02</b><small>Mon</small></li><li class="day"><b>01</b><small>Sun</small></li><li class="day"><b>01</b><small>Sun</small></li><li class="day"><b>02</b><small>Mon</small></li><li class="day"><b>01</b><small>Sun</small></li>
</ol><div class="foot"></div></section>

<section class="month g2"><h2>AUG</h2><ol class="days">
<li class="day"><b>01</b><small>Wed</small></li><li class="day"><b>02</b><small>Thu</small></li><li class="day"><b>01</b><small>Wed</small></li><li class="day"><b>02</b><small>Thu</small></li><li class="day mark"><b>01</b><small>Wed</small></li><li class="day mark"><b>02</b><small>Thu</small></li><li class="day"><b>01</b><small>Wed</small></li><li class="day"><b>01</b><small>Wed</small></li><li class="day"><b>02</b><small>Thu</small></li><li class="day"><b>01</b><small>Wed</small></li><li class="day mark"><b>02</b><small>Thu</small></li><li class="day mark"><b>01</b><small>Wed</small></li><li class="day"><b>02</b><small>Thu</small></li><li class="day mark"><b>01</b><small>Wed</small></li><li class="day mark"><b>01</b><small>Wed</small></li><li class="day"><b>02</b><small>Thu</small></li><li class="day"><b>01</b><small>Wed</small></li><li class="day"><b>02</b><small>Thu</small></li><li class="day"><b>01</b><small>Wed</small></li><li class="day mark"><b>02</b><small>Thu</small></li><li class="day mark"><b>01</b><small>Wed</small></li><li class="day"><b>01</b><small>Wed</small></li><li class="day"><b>02</b><small>Thu</small></li><li class="day mark"><b>01</b><small>Wed</small></li><li class="day mark"><b>02</b><small>Thu</small></li><li class="day mark"><b>01</b><small>Wed</small></li><li class="day"><b>02</b><small>Thu</small></li><li class="day"><b>01</b><small>Wed</small></li><li class="day"><b>01</b><small>Wed</small></li><li class="day"><b>02</b><small>Thu</small></li><li class="day"><b>01</b><small>Wed</small></li>
</ol><div class="foot"></div></section>

<section class="month o1"><h2>SEP</h2><ol class="days">
<li class="day hol"><b>01</b><small>Sat</small></li><li class="day hol"><b>02</b><small>Sun</small></li><li class="day"><b>01</b><small>Sat</small></li><li class="day"><b>02</b><small>Sun</small></li><li class="day"><b>01</b><small>Sat</small></li><li class="day mark"><b>02</b><small>Sun</small></li><li class="day mark"><b>01</b><small>Sat</small></li><li class="day"><b>01</b><small>Sat</small></li><li class="day"><b>02</b><small>Sun</small></li><li class="day"><b>01</b><small>Sat</small></li><li class="day mark"><b>02</b><small>Sun</small></li><li class="day mark"><b>01</b><small>Sat</small></li><li class="day"><b>02</b><small>Sun</small></li><li class="day mark"><b>01</b><small>Sat</small></li><li class="day mark"><b>01</b><small>Sat</small></li><li class="day"><b>02</b><small>Sun</small></li><li class="day"><b>01</b><small>Sat</small></li><li class="day"><b>02</b><small>Sun</small></li><li class="day"><b>01</b><small>Sat</small></li><li class="day mark"><b>02</b><small>Sun</small></li><li class="day mark"><b>01</b><small>Sat</small></li><li class="day"><b>01</b><small>Sat</small></li><li class="day"><b>02</b><small>Sun</small></li><li class="day"><b>01</b><small>Sat</small></li><li class="day"><b>02</b><small>Sun</small></li><li class="day mark"><b>01</b><small>Sat</small></li><li class="day mark"><b>02</b><small>Sun</small></li><li class="day"><b>01</b><small>Sat</small></li><li class="day"><b>01</b><small>Sat</small></li><li class="day"><b>02</b><small>Sun</small></li><li class="day"><b>01</b><small>Sat</small></li>
</ol><div class="foot"></div></section>

<section class="month o2"><h2>OCT</h2><ol class="days">
<li class="day"><b>01</b><small>Mon</small></li><li class="day"><b>02</b><small>Tue</small></li><li class="day"><b>01</b><small>Mon</small></li><li class="day"><b>02</b><small>Tue</small></li><li class="day"><b>01</b><small>Mon</small></li><li class="day"><b>02</b><small>Tue</small></li><li class="day mark"><b>01</b><small>Mon</small></li><li class="day mark"><b>01</b><small>Mon</small></li><li class="day"><b>02</b><small>Tue</small></li><li class="day"><b>01</b><small>Mon</small></li><li class="day mark"><b>02</b><small>Tue</small></li><li class="day mark"><b>01</b><small>Mon</small></li><li class="day"><b>02</b><small>Tue</small></li><li class="day"><b>01</b><small>Mon</small></li><li class="day mark"><b>01</b><small>Mon</small></li><li class="day mark"><b>02</b><small>Tue</small></li><li class="day"><b>01</b><small>Mon</small></li><li class="day"><b>02</b><small>Tue</small></li><li class="day mark"><b>01</b><small>Mon</small></li><li class="day mark"><b>02</b><small>Tue</small></li><li class="day"><b>01</b><small>Mon</small></li><li class="day"><b>01</b><small>Mon</small></li><li class="day"><b>02</b><small>Tue</small></li><li class="day"><b>01</b><small>Mon</small></li><li class="day"><b>02</b><small>Tue</small></li><li class="day"><b>01</b><small>Mon</small></li><li class="day mark"><b>02</b><small>Tue</small></li><li class="day mark"><b>01</b><small>Mon</small></li><li class="day"><b>01</b><small>Mon</small></li><li class="day"><b>02</b><small>Tue</small></li><li class="day"><b>01</b><small>Mon</small></li>
</ol><div class="foot"></div></section>

<section class="month r1"><h2>NOV</h2><ol class="days">
<li class="day"><b>01</b><small>Thu</small></li><li class="day"><b>02</b><small>Fri</small></li><li class="day mark"><b>01</b><small>Thu</small></li><li class="day mark"><b>02</b><small>Fri</small></li><li class="day mark"><b>01</b><small>Thu</small></li><li class="day mark"><b>02</b><small>Fri</small></li><li class="day mark"><b>01</b><small>Thu</small></li><li class="day mark"><b>01</b><small>Thu</small></li><li class="day mark"><b>02</b><small>Fri</small></li><li class="day"><b>01</b><small>Thu</small></li><li class="day mark"><b>02</b><small>Fri</small></li><li class="day mark"><b>01</b><small>Thu</small></li><li class="day"><b>02</b><small>Fri</small></li><li class="day"><b>01</b><small>Thu</small></li><li class="day"><b>01</b><small>Thu</small></li><li class="day mark"><b>02</b><small>Fri</small></li><li class="day mark"><b>01</b><small>Thu</small></li><li class="day mark"><b>02</b><small>Fri</small></li><li class="day mark"><b>01</b><small>Thu</small></li><li class="day"><b>02</b><small>Fri</small></li><li class="day"><b>01</b><small>Thu</small></li><li class="day"><b>01</b><small>Thu</small></li><li class="day mark"><b>02</b><small>Fri</small></li><li class="day mark"><b>01</b><small>Thu</small></li><li class="day mark"><b>02</b><small>Fri</small></li><li class="day mark"><b>01</b><small>Thu</small></li><li class="day mark"><b>02</b><small>Fri</small></li><li class="day mark"><b>01</b><small>Thu</small></li><li class="day mark"><b>01</b><small>Thu</small></li><li class="day"><b>02</b><small>Fri</small></li><li class="day"><b>01</b><small>Thu</small></li>
</ol><div class="foot"></div></section>

<section class="month r2"><h2>DEC</h2><ol class="days">
<li class="day hol"><b>01</b><small>Sat</small></li><li class="day hol"><b>02</b><small>Sun</small></li><li class="day"><b>01</b><small>Sat</small></li><li class="day"><b>02</b><small>Sun</small></li><li class="day"><b>01</b><small>Sat</small></li><li class="day"><b>02</b><small>Sun</small></li><li class="day"><b>01</b><small>Sat</small></li><li class="day"><b>01</b><small>Sat</small></li><li class="day"><b>02</b><small>Sun</small></li><li class="day"><b>01</b><small>Sat</small></li><li class="day"><b>02</b><small>Sun</small></li><li class="day"><b>01</b><small>Sat</small></li><li class="day"><b>02</b><small>Sun</small></li><li class="day"><b>01</b><small>Sat</small></li><li class="day"><b>01</b><small>Sat</small></li><li class="day"><b>02</b><small>Sun</small></li><li class="day"><b>01</b><small>Sat</small></li><li class="day"><b>02</b><small>Sun</small></li><li class="day"><b>01</b><small>Sat</small></li><li class="day"><b>02</b><small>Sun</small></li><li class="day"><b>01</b><small>Sat</small></li><li class="day"><b>01</b><small>Sat</small></li><li class="day"><b>02</b><small>Sun</small></li><li class="day"><b>01</b><small>Sat</small></li><li class="day"><b>02</b><small>Sun</small></li><li class="day"><b>01</b><small>Sat</small></li><li class="day"><b>02</b><small>Sun</small></li><li class="day"><b>01</b><small>Sat</small></li><li class="day"><b>01</b><small>Sat</small></li><li class="day"><b>02</b><small>Sun</small></li><li class="day"><b>01</b><small>Sat</small></li>
</ol><div class="foot"></div></section>

<h1 class="title">XYZ Co 2012 Planner</h1>
</main>
</body>
</html>
```